Flyer / Mailer for Business Debt Relief Business - Tillbrook Partners 6" x 11"

We need a 6" x 11" double sided flyer. This will be sent out to potential customers with high interest business loans. We would like the design to coordinate with the colors of our logo. I have included a mock up that we sketched out. I have also included a file of a mailer we received that we would like to use as a template (not colors or fonts, just set up). I have also included an .ai file of our logo.

```html
<!DOCTYPE html>
<html lang="en">
<head>
<meta charset="utf-8">
<title>Tillbrook Partners – Debt Relief Mailer</title>
<link href="https://fonts.googleapis.com/css2?family=Montserrat:wght@400;500;600;700;800&display=swap" rel="stylesheet">
<style>
  :root {
    --blue: #0a7fc7;
    --deep-blue: #1b5d96;
    --green: #77bc43;
    --dark-green: #5fa334;
    --charcoal: #3d3d3d;
    --ink: #1d1d1d;
    --paper: #ffffff;
    --backdrop: #d9dadc;
  }
  * { box-sizing: border-box; margin: 0; padding: 0; }
  html, body { width: 1078px; height: 1200px; overflow: hidden; }
  body {
    background: var(--backdrop);
    font-family: "Montserrat", Arial, sans-serif;
    position: relative;
  }
  .card {
    position: absolute;
    left: 60px;
    width: 957px;
    height: 531px;
    background: var(--paper);
    overflow: hidden;
  }
  .card--front { top: 42px; }
  .card--back { top: 627px; }
  .card-shapes { position: absolute; inset: 0; width: 100%; height: 100%; }
  .abs { position: absolute; }

  /* front */
  .headline {
    left: 27px; top: 26px;
    color: var(--paper);
    font-weight: 800; font-size: 40px; line-height: 44px;
  }
  .subhead {
    left: 27px; top: 134px;
    color: var(--green);
    font-weight: 600; font-size: 23px; line-height: 22px;
  }
  .photo-slot {
    border: 3px solid var(--paper);
  }
  .photo-slot--growth { left: 21px; top: 234px; width: 165px; height: 94px;
    background: linear-gradient(135deg, #1560a8, #3b8fd6 60%, #e9eef4); }
  .photo-slot--cash { left: 21px; top: 346px; width: 165px; height: 94px;
    background: linear-gradient(135deg, #2a3a3f, #6f8a77 55%, #c9d4c6); }
  .photo-slot--advisor { left: 605px; top: 124px; width: 279px; height: 334px;
    background: linear-gradient(160deg, #f2f3f5 0%, #d9dde2 40%, #4a5260 75%, #2f3540 100%); }
  .brand {
    display: flex; align-items: center; gap: 8px;
    color: var(--charcoal);
    font-weight: 500; font-size: 17px; letter-spacing: 0.5px;
  }
  .brand-square { width: 16px; height: 16px; background: var(--green); }
  .brand--front { left: 452px; top: 178px; }
  .question {
    left: 222px; top: 228px;
    color: var(--charcoal);
    font-weight: 600; font-size: 19px; line-height: 20px;
  }
  .help {
    left: 222px; top: 268px;
    color: var(--blue);
    font-weight: 800; font-size: 31px;
  }
  .benefits {
    left: 224px; top: 313px;
    list-style: none;
    color: var(--ink);
    font-size: 12.5px; line-height: 15.6px;
  }
  .benefits li { display: flex; align-items: center; gap: 9px; }
  .benefits svg { width: 8px; height: 8px; flex: none; }
  .contact-label { color: var(--green); font-weight: 700; font-size: 17px; line-height: 21px; }
  .contact-value { color: var(--paper); font-weight: 700; font-size: 17px; line-height: 21px; }
  .visit { left: 27px; top: 469px; }
  .call { left: 290px; top: 469px; }
  .mail { left: 662px; top: 480px; display: flex; align-items: center; gap: 9px; }

  /* back */
  .back-brand {
    left: 0; width: 376px; top: 40px;
    display: flex; flex-direction: column; align-items: center; gap: 18px;
    color: var(--charcoal);
    font-weight: 500; font-size: 23px; letter-spacing: 1px;
  }
  .back-brand .brand-square { width: 56px; height: 56px; }
  .address {
    left: 0; width: 376px; top: 186px;
    text-align: center;
    color: var(--ink);
    font-weight: 600; font-size: 17.5px; line-height: 21.5px;
  }
  .relief-title {
    left: 35px; top: 284px;
    color: var(--paper); font-weight: 700;
  }
  .relief-title span { display: block; }
  .relief-title .line-1 { font-size: 23px; line-height: 30px; }
  .relief-title .line-2 { font-size: 28.5px; line-height: 34px; }
  .relief-body {
    left: 35px; top: 357px; width: 320px;
    color: var(--ink);
    font-weight: 500; font-size: 19.5px; line-height: 24px;
  }
  .back-contacts {
    left: 35px; top: 472px;
    color: var(--paper);
    font-weight: 500; font-size: 14px; line-height: 18.5px;
  }
  .back-contacts .row { display: flex; gap: 12px; }
  .back-contacts .item { display: flex; align-items: center; gap: 4px; }
  .back-contacts svg { width: 12px; height: 12px; }
  .stamp-box {
    left: 864px; top: 30px; width: 63px; height: 82px;
    border: 2px solid var(--charcoal);
  }
</style>
</head>
<body>

<section class="card card--front">
  <svg class="card-shapes" viewBox="0 0 1196 664" preserveAspectRatio="none" aria-hidden="true">
    <rect x="0" y="0" width="1196" height="155" fill="var(--blue)"/>
    <polygon points="705,0 1196,0 1196,490 1105,400 1105,110 815,110" fill="var(--green)"/>
    <polygon points="705,0 815,110 1105,110 1105,400 1196,490 1196,470 1115,395 1115,100 820,100 718,0" fill="var(--paper)" opacity="0.9"/>
    <polygon points="1115,100 1196,20 1196,60 1125,110" fill="var(--dark-green)"/>
    <polygon points="0,155 558,155 495,269 0,269" fill="var(--charcoal)"/>
    <rect x="0" y="269" width="266" height="304" fill="var(--green)"/>
    <polygon points="712,470 712,573 815,573" fill="var(--blue)"/>
    <polygon points="712,470 760,540 730,573 712,573" fill="var(--deep-blue)"/>
    <rect x="0" y="573" width="1196" height="91" fill="var(--deep-blue)"/>
  </svg>

  <h1 class="abs headline">Helping business focus<br>what matters!</h1>
  <p class="abs subhead">we understand that merchant<br>cash advance loans can be<br>a burden on your bsuiness</p>

  <div class="abs photo-slot photo-slot--growth" role="img" aria-label="Businessman beside a rising bar chart"></div>
  <div class="abs photo-slot photo-slot--cash" role="img" aria-label="Hands counting banknotes"></div>
  <div class="abs photo-slot--advisor" role="img" aria-label="Smiling consultant in a suit holding a tablet"></div>

  <div class="abs brand brand--front"><span class="brand-square"></span>Tillbrook Partners</div>

  <p class="abs question">Overwhelmed by<br>daily / weekly payments?</p>
  <p class="abs help">WE CAN HELP!</p>

  <ul class="abs benefits">
    <li><svg viewBox="0 0 8 8"><path d="M0 0H8V8L5 5V3H3Z" fill="var(--blue)"/></svg>This is not a loan, WE ARE NOT LENDERS!</li>
    <li><svg viewBox="0 0 8 8"><path d="M0 0H8V8L5 5V3H3Z" fill="var(--blue)"/></svg>Improve your business cash flow immedietly</li>
    <li><svg viewBox="0 0 8 8"><path d="M0 0H8V8L5 5V3H3Z" fill="var(--blue)"/></svg>Move payments to one monthly amount</li>
    <li><svg viewBox="0 0 8 8"><path d="M0 0H8V8L5 5V3H3Z" fill="var(--blue)"/></svg>Reduce the amount you are paying out monthly</li>
    <li><svg viewBox="0 0 8 8"><path d="M0 0H8V8L5 5V3H3Z" fill="var(--blue)"/></svg>Strategic alternatives to high interset loans</li>
    <li><svg viewBox="0 0 8 8"><path d="M0 0H8V8L5 5V3H3Z" fill="var(--blue)"/></svg>Fast, confedintial business debt relief</li>
    <li><svg viewBox="0 0 8 8"><path d="M0 0H8V8L5 5V3H3Z" fill="var(--blue)"/></svg>No-oblisction consultation</li>
    <li><svg viewBox="0 0 8 8"><path d="M0 0H8V8L5 5V3H3Z" fill="var(--blue)"/></svg>Absolutely no credit polls</li>
    <li><svg viewBox="0 0 8 8"><path d="M0 0H8V8L5 5V3H3Z" fill="var(--blue)"/></svg>No colleteral, no financials</li>
  </ul>

  <div class="abs visit">
    <p class="contact-label">Visit Our Website</p>
    <p class="contact-value">tillbrookpartners.com</p>
  </div>
  <div class="abs call">
    <p class="contact-label">Call Now for free consultation</p>
    <p class="contact-label">with our experts <span class="contact-value">&nbsp;844-555-0172</span></p>
  </div>
  <div class="abs mail">
    <svg width="20" height="13" viewBox="0 0 20 13" aria-hidden="true"><rect width="20" height="13" fill="var(--green)"/><path d="M0 0L10 7L20 0" stroke="var(--deep-blue)" stroke-width="1.5" fill="none"/></svg>
    <span class="contact-value">info@tillbrookpartners.com</span>
  </div>
</section>

<section class="card card--back">
  <svg class="card-shapes" viewBox="0 0 957 531" preserveAspectRatio="none" aria-hidden="true">
    <rect x="0" y="259" width="376" height="7" fill="var(--blue)"/>
    <rect x="0" y="269" width="376" height="197" fill="var(--green)"/>
    <rect x="0" y="466" width="376" height="65" fill="var(--deep-blue)"/>
    <rect x="379" y="0" width="3" height="531" fill="var(--blue)"/>
  </svg>

  <div class="abs back-brand"><span class="brand-square"></span>Tillbrook Partners</div>

  <p class="abs address">1450 Harlow Ave<br>Fenmore, Ridge County 76099<br>USA</p>

  <h2 class="abs relief-title"><span class="line-1">Strategic Debt Relief For</span><span class="line-2">Business Of All Sizes</span></h2>
  <p class="abs relief-body">Stop taking out loans to pay off other loans take back your business cash flow, and focus on what matters.</p>

  <div class="abs back-contacts">
    <div class="row">
      <span class="item"><svg viewBox="0 0 12 12" aria-hidden="true"><path d="M2 1L4.5 1L5.5 4L4 5C4.8 6.6 5.8 7.6 7 8L8 6.5L11 7.5V10C11 10.6 10.6 11 10 11C5 11 1 7 1 2C1 1.4 1.4 1 2 1Z" fill="var(--green)"/></svg>844-555-0172</span>
      <span class="item"><svg viewBox="0 0 12 12" aria-hidden="true"><rect y="2" width="12" height="8" fill="var(--green)"/><path d="M0 2L6 6.5L12 2" stroke="var(--deep-blue)" fill="none"/></svg>info@tillbrookpartners.com</span>
    </div>
    <div class="row">
      <span class="item"><svg viewBox="0 0 12 12" aria-hidden="true"><circle cx="6" cy="6" r="5" fill="none" stroke="var(--green)" stroke-width="1.3"/><ellipse cx="6" cy="6" rx="2.2" ry="5" fill="none" stroke="var(--green)"/><path d="M1 6H11" stroke="var(--green)"/></svg>tillbrookpartners.com</span>
    </div>
  </div>

  <div class="abs stamp-box"></div>
</section>

</body>
</html>
```